Business Card Design

We are looking for a double sided business card.

On one side would be our logo

On the Other Side

Martin Kolby
Sales and Marketing

Phone/Text Logo and 530-418-2763
Email Logo and info@plumvalepets.com
Website Logo and www.plumvalepets.com
Facebook Logo and plumvale pets
Instagram Logo and plumvale_pets

Target Market(s)

Pet owners

Contact Information for Business Card

In project description

Requirements
Must have
• Logo

```html
<!DOCTYPE html>
<html lang="en">
<head>
<meta charset="utf-8">
<title>Plumvale Pets – Business Card</title>
<link rel="stylesheet" href="https://fonts.googleapis.com/css2?family=Roboto:wght@400;500;700;900&display=swap">
<style>
  :root {
    --backdrop: #1b1c1e;
    --card: #2b2b2c;
    --card-deep: #232324;
    --white: #f2f2f2;
    --soft: #d9d9d9;
    --orange: #f7a21b;
    --yellow: #ffd20a;
    --divider: #cfcfcf;
  }
  * { box-sizing: border-box; margin: 0; padding: 0; }
  html, body { width: 1200px; height: 840px; overflow: hidden; }
  body {
    background: var(--backdrop);
    font-family: "Roboto", Arial, sans-serif;
    display: flex;
    flex-direction: column;
    align-items: center;
    justify-content: center;
    gap: 40px;
  }
  .card-edge {
    width: 620px;
    height: 356px;
    border-radius: 26px;
    padding: 0 0 4px 0;
    background: linear-gradient(90deg, var(--yellow), var(--orange));
  }
  .card {
    position: relative;
    width: 100%;
    height: 100%;
    border-radius: 26px;
    background: linear-gradient(135deg, var(--card), var(--card-deep));
    color: var(--white);
    overflow: hidden;
  }

  /* Front */
  .front-brand {
    position: absolute;
    left: 48px;
    bottom: 52px;
  }
  .brand-name {
    font-weight: 900;
    font-size: 50px;
    letter-spacing: 1px;
    text-transform: uppercase;
    color: var(--white);
    line-height: 1;
    display: flex;
    align-items: center;
    gap: 14px;
  }
  .brand-dot {
    width: 22px; height: 22px;
    border-radius: 50%;
    background: var(--orange);
    flex: none;
  }
  .front-url {
    margin-top: 14px;
    font-size: 15px;
    font-weight: 500;
    letter-spacing: 5px;
    text-transform: uppercase;
    color: var(--orange);
  }

  /* Back */
  .back-brand {
    position: absolute;
    left: 40px;
    top: 128px;
    width: 230px;
  }
  .back-brand .brand-name { font-size: 34px; gap: 10px; }
  .back-brand .brand-dot { width: 16px; height: 16px; }
  .back-divider {
    position: absolute;
    left: 292px;
    top: 60px;
    width: 1px;
    height: 190px;
    background: var(--divider);
  }
  .contact-block {
    position: absolute;
    left: 320px;
    top: 62px;
  }
  .person-name {
    font-weight: 900;
    font-size: 27px;
    color: var(--orange);
    text-transform: uppercase;
    line-height: 1.1;
  }
  .person-role {
    font-size: 17px;
    color: var(--white);
    margin-top: 2px;
  }
  .contact-list {
    list-style: none;
    margin-top: 30px;
    font-size: 17px;
    line-height: 1.55;
  }
  .contact-list li { display: flex; align-items: center; gap: 10px; }
  .contact-list svg { width: 16px; height: 16px; flex: none; }
  .social-row {
    position: absolute;
    left: 320px;
    bottom: 42px;
    display: flex;
    gap: 28px;
    font-size: 17px;
  }
  .social-row span { display: flex; align-items: center; gap: 8px; }
  .social-mark {
    width: 14px; height: 14px;
    border-radius: 3px;
    background: var(--orange);
  }
  .social-mark.round { border-radius: 50%; }
</style>
</head>
<body>

  <section class="card-edge">
    <div class="card card-front">
      <div class="front-brand">
        <div class="brand-name"><span class="brand-dot"></span>Plumvale Pets</div>
        <div class="front-url">www.plumvalepets.com</div>
      </div>
    </div>
  </section>

  <section class="card-edge">
    <div class="card card-back">
      <div class="back-brand">
        <div class="brand-name"><span class="brand-dot"></span>Plumvale Pets</div>
      </div>

      <div class="back-divider"></div>

      <div class="contact-block">
        <h1 class="person-name">Martin Kolby</h1>
        <p class="person-role">Sales and Marketing</p>
        <ul class="contact-list">
          <li>
            <svg viewBox="0 0 16 16" aria-hidden="true"><path fill="#f7a21b" d="M3.5 1.5l2.5 0 1 3.5-1.6 1.2a8 8 0 0 0 4.4 4.4L11 9l3.5 1v2.5c0 1-1 2-2 2A11 11 0 0 1 1.5 3.5c0-1 1-2 2-2z"/></svg>
            530-418-2763
          </li>
          <li>
            <svg viewBox="0 0 16 16" aria-hidden="true"><rect x="1" y="3" width="14" height="10" rx="1.5" fill="#f7a21b"/><path d="M1.5 4l6.5 5 6.5-5" fill="none" stroke="#2b2b2c" stroke-width="1.4"/></svg>
            info@plumvalepets.com
          </li>
          <li>
            <svg viewBox="0 0 16 16" aria-hidden="true"><circle cx="8" cy="8" r="7" fill="#f7a21b"/><path d="M1 8h14M8 1c-3 3.5-3 10.5 0 14M8 1c3 3.5 3 10.5 0 14" fill="none" stroke="#2b2b2c" stroke-width="1.1"/></svg>
            www.plumvalepets.com
          </li>
        </ul>
      </div>

      <div class="social-row">
        <span><i class="social-mark"></i>plumvale pets</span>
        <span><i class="social-mark round"></i>plumvale_pets</span>
      </div>
    </div>
  </section>

</body>
</html>
```